Lien Post Card - (5.5 x 8.5)

FRONT OF POSTCARD
Is a Property Lien Putting Your Home at Risk?
HOA Liens • Tax Liens • Municipal Charges • Other Property-Related Liens
You may have options to resolve outstanding liens and protect your home.
A Refinance or Home Equity Line of Credit (HELOC) may help you:
✔ Pay off qualifying liens
✔ Consolidate debt into one manageable payment
✔ Access your home's equity
✔ Improve your financial flexibility
✔ Avoid additional penalties, fees, or collection actions
Don't wait until the situation becomes more difficult.
Call today for a confidential review of your options.
Bluecove Lending Group, Inc.
(800) 641-2907 x 42
www.bluecovelending.com
NMLS #738150
BACK OF POSTCARD
Your Home Equity Could Be the Solution
If you have received notices regarding:
• Delinquent Property Taxes
• HOA or Condo Association Assessments
• Municipal Utility Liens
• Special Assessments
• Other Property-Related Obligations
You may qualify for financing options designed to help satisfy those obligations and bring your property current.
Our experienced mortgage professionals can review your situation and discuss available programs, including:
• Cash-Out Refinancing
• Home Equity Lines of Credit (HELOCs)
• Home Equity Loans
• Debt Consolidation Solutions
Free Consultation • No Obligation
Contact Marcus Whitfield today at (800) 641-2907 x42 or mwhitfield@bluecovelending.com (NMLS #84617)

```html
<!DOCTYPE html>
<html lang="en">
<head>
<meta charset="utf-8">
<title>Lien Postcard – Front and Back</title>
<link href="https://fonts.googleapis.com/css2?family=Source+Sans+3:wght@600;700;800&display=swap" rel="stylesheet">
<style>
  :root{
    --navy:#0b5188;
    --gold:#d29c35;
    --mist:#ebeef2;
    --ink:#111111;
    --paper:#ffffff;
    --backdrop:#6f6f69;
  }
  *{margin:0;padding:0;box-sizing:border-box}
  html,body{width:1200px;height:1200px;overflow:hidden}
  body{background:var(--backdrop);font-family:"Source Sans 3",sans-serif;color:var(--ink);position:relative}
  .card{position:absolute;top:232px;width:489px;height:744px;background:var(--paper);box-shadow:0 4px 14px rgba(0,0,0,.35);overflow:hidden}
  .card--front{left:101px}
  .card--back{left:617px}
  .abs{position:absolute;line-height:1}
  .center{left:0;right:0;text-align:center}
  .right{right:28px;text-align:right}

  /* front */
  .front-header{position:absolute;left:0;top:0;width:100%;height:113px;background:var(--navy)}
  .front-title{color:#fff;font-weight:700;font-size:32px;line-height:34px;top:23px}
  .gold-rule{position:absolute;left:0;width:100%;background:var(--gold)}
  .lien-band{position:absolute;left:0;top:119px;width:100%;height:166px;background:var(--mist)}
  .lien-list{list-style:none;position:absolute;left:29px;top:146px;font-weight:700;font-size:17.5px}
  .lien-list li{height:30px}
  .illustration{position:absolute;left:268px;top:127px;width:194px;height:158px;border-radius:80px 80px 10px 10px;background:radial-gradient(circle at 50% 55%,#5bb4e6 0 38%,#1d5a8c 39% 44%,transparent 45%),linear-gradient(#ebeef2,#ebeef2)}
  .lead{font-weight:700;font-size:22.5px;line-height:24px}
  .intro{font-weight:700;font-size:14px;line-height:15.5px}
  .checks{list-style:none;position:absolute;font-weight:700;font-size:14px}
  .checks li{height:24px}
  .checks .tick{color:var(--navy);margin-right:2px}
  .cta-band{position:absolute;left:0;top:554px;width:100%;height:63px;background:var(--navy)}
  .cta{color:#fff;font-weight:700;font-size:17px;line-height:22px;top:565px}
  .brand{position:absolute;left:26px;top:660px;display:flex;align-items:center;gap:7px;font-weight:700;font-size:14px;color:var(--navy);line-height:1.1;width:170px}
  .brand-dot{width:22px;height:22px;border-radius:50%;background:var(--navy);flex:none}
  .phone{font-weight:700;font-size:26px}
  .web{font-weight:700;font-size:20.5px}
  .nmls{font-weight:700;font-size:13px}

  /* back */
  .back-title{color:var(--navy);font-weight:700;font-size:32.5px;line-height:34px;top:28px}
  .notice-band{position:absolute;left:0;top:119px;width:100%;height:154px;background:var(--mist)}
  .notice-intro{left:23px;top:132px;font-weight:700;font-size:16px}
  .notice-list{list-style:none;position:absolute;left:23px;top:160px;font-weight:700;font-size:14px}
  .notice-list li{height:21.3px}
  .photo-couple{position:absolute;left:301px;top:119px;width:173px;height:154px;background:linear-gradient(135deg,#e6e2dc,#a89e94 55%,#6b625c)}
  .navy-rule{position:absolute;left:0;top:560px;width:100%;height:2px;background:var(--navy)}
  .photo-advisor{position:absolute;left:23px;top:584px;width:112px;height:120px;background:linear-gradient(#ececec,#b8b8b8 60%,#2c2c2c)}
  .offer{color:var(--navy);font-weight:700;font-size:20px;top:583px}
  .contact{font-weight:700;font-size:19px;top:619px}
  .bar{position:absolute;top:720px;height:24px;width:50%}
  .bar--gold{left:0;background:var(--gold)}
  .bar--navy{right:0;background:var(--navy)}
</style>
</head>
<body>

<section class="card card--front">
  <div class="front-header"></div>
  <h1 class="abs center front-title">Is a Property Lien Putting<br>Your Home at Risk?</h1>
  <div class="gold-rule" style="top:113px;height:6px"></div>
  <div class="lien-band"></div>
  <ul class="lien-list">
    <li>• HOA Liens</li>
    <li>• Tax Liens</li>
    <li>• Municipal Charges</li>
    <li>• Other Property-Related Liens</li>
  </ul>
  <div class="illustration" role="img" aria-label="Illustration of a house held in a hand, surrounded by shield, phone and document icons"></div>

  <p class="abs center lead" style="top:296px">You may have options to resolve<br>outstanding liens and protect your home.</p>
  <p class="abs intro" style="left:30px;top:366px">A Refinance or Home Equity Line of<br>Credit (HELOC) may help you:</p>
  <ul class="checks" style="left:29px;top:414px">
    <li><span class="tick">✓</span>Pay off qualifying liens</li>
    <li><span class="tick">✓</span>Consolidate debt into one manageable payment</li>
    <li><span class="tick">✓</span>Access your home's equity</li>
    <li><span class="tick">✓</span>Improve your financial flexibility</li>
    <li><span class="tick">✓</span>Avoid additional penalties, fees, or collection actions</li>
  </ul>

  <div class="gold-rule" style="top:548px;height:6px"></div>
  <div class="cta-band"></div>
  <p class="abs center cta">Don't wait until the situation becomes more difficult.<br>Call today for a confidential review of your options.</p>

  <div class="brand"><span class="brand-dot"></span><span>Bluecove Lending Group, Inc.</span></div>
  <p class="abs right phone" style="top:646px">(800) 641-2907 x 42</p>
  <p class="abs right web" style="top:673px">www.bluecovelending.com</p>
  <p class="abs right nmls" style="top:700px">NMLS #738150</p>
</section>

<section class="card card--back">
  <h1 class="abs center back-title">Your Home Equity Could<br>Be the Solution</h1>
  <div class="notice-band"></div>
  <p class="abs notice-intro">If you have received notices regarding:</p>
  <ul class="notice-list">
    <li>• Delinquent Property Taxes</li>
    <li>• HOA or Condo Association Assessments</li>
    <li>• Municipal Utility Liens</li>
    <li>• Special Assessments</li>
    <li>• Other Property-Related Obligations</li>
  </ul>
  <div class="photo-couple" role="img" aria-label="Photo of a worried couple reviewing bills at a kitchen table"></div>
  <div class="gold-rule" style="top:273px;height:5px"></div>

  <p class="abs center lead" style="top:305px">You may qualify for financing options<br>designed to help satisfy those obligations<br>and bring your property current.</p>
  <p class="abs intro" style="left:23px;top:406px">Our experienced mortgage professionals can review<br>your situation and discuss available programs, including:</p>
  <ul class="checks" style="left:23px;top:452px">
    <li><span class="tick">✓</span>Cash-Out Refinancing</li>
    <li><span class="tick">✓</span> Home Equity Lines of Credit (HELOCs)</li>
    <li><span class="tick">✓</span> Home Equity Loans</li>
    <li><span class="tick">✓</span> Debt Consolidation Solutions</li>
  </ul>

  <div class="navy-rule"></div>
  <div class="photo-advisor" role="img" aria-label="Portrait photo of loan officer Marcus Whitfield"></div>
  <p class="abs right offer" style="right:29px">Free Consultation • No Obligation</p>
  <p class="abs right contact" style="right:29px">Contact Marcus Whitfield today at</p>
  <p class="abs right phone" style="right:29px;top:646px">(800) 641-2907 x 42</p>
  <p class="abs right web" style="right:29px;top:673px">www.bluecovelending.com</p>
  <p class="abs right nmls" style="right:29px;top:700px">NMLS #738150</p>
  <div class="bar bar--gold"></div>
  <div class="bar bar--navy"></div>
</section>

</body>
</html>
```